Etiketten-Design für Ober- & Rückseite eines Produktes
Zielgruppe
Bei diesem Produkt handelt es sich um eine hochwertige, vegane, essfertige Polenta in einer rechteckigen Tiefziehschale. Wir möchten ein Etikett auf der Oberseite sowie auf der Rückseite. Das Rückseiten Etikett enthält Zutaten, Nähwerttabelle, Rechtliche Hinweiße.
Bei diesem Produkt sehen wir den Kunden der eine schnelle, gesunde, nahrhafte, leicht zuzubereitende und schmackhafte Beilage zu vielen Speisen oder auch als Hauptgericht sucht.
Das gewünschte Format sowie weitere Elemente wie unser Firmenlogo und einen weiteren Eigenmarken Namen finden Sie in den Anhängen.
Aufgabenstellung
Da unserer Polenta Vegan ist sollte dies auch besonders Ausgelobt sein. Unter folgenden Produktnamen möchten wir Designs:
'Polenta Tessara Pura'
'Polenta Corvella La Scelta Dorata'
'Polenta Tessara, Gallo Verde'
Auf den Rückseitenetiketten sollte neben unserem Firmennamen und Logo, sich auch das Oberösterreiche Wappen finden.
Bei der Eigenmarke ' Feinwahl' nur den Schriftzug verwenden!

```html
<!DOCTYPE html>
<html lang="de">
<head>
<meta charset="utf-8">
<title>Polenta Etiketten – Feinwahl</title>
<link rel="stylesheet" href="https://fonts.googleapis.com/css2?family=Kaushan+Script&family=Montserrat:wght@600;700;800&display=swap">
<style>
  :root {
    --backdrop: #b3b3b3;
    --leaf-green: #8db443;
    --tomato-red: #b22024;
    --label-white: #ffffff;
    --ink: #1a1a1a;
  }
  html, body {
    margin: 0;
    padding: 0;
    overflow: hidden;
  }
  body {
    width: 1200px;
    height: 3717px;
    background: var(--backdrop);
    position: relative;
  }
  .label {
    position: absolute;
    display: block;
  }
  .label--hero { left: 330px; top: 250px; width: 540px; height: 600px; }
  .label--tessara-pura { left: 267px; top: 1153px; width: 677px; height: 752px; }
  .label--corvella { left: 267px; top: 1958px; width: 677px; height: 752px; }
  .label--gallo-verde { left: 267px; top: 2762px; width: 677px; height: 752px; }

  .band-top { fill: var(--leaf-green); }
  .band-bottom { fill: var(--tomato-red); }
  .field { fill: var(--label-white); }
  .maker-dot { fill: var(--tomato-red); }
  .maker-name {
    font-family: "Montserrat", sans-serif;
    font-weight: 700;
    font-size: 17px;
    fill: var(--tomato-red);
  }
  .product-word {
    font-family: "Kaushan Script", cursive;
    font-size: 82px;
    fill: var(--leaf-green);
  }
  .variety {
    font-family: "Montserrat", sans-serif;
    font-weight: 600;
    font-size: 22px;
    letter-spacing: 1.2px;
    fill: var(--ink);
  }
  .brand-name {
    font-family: "Montserrat", sans-serif;
    font-weight: 800;
    font-size: 68px;
    fill: var(--leaf-green);
  }
  .vegan-claim {
    font-family: "Montserrat", sans-serif;
    font-weight: 700;
    font-size: 20px;
    fill: var(--label-white);
  }
</style>
</head>
<body>

<svg class="label label--hero" viewBox="0 0 451 501" aria-label="Etikett Polenta Tessara Pura">
  <rect class="field" width="451" height="501"/>
  <path class="band-top" d="M0,0 H451 V32 C300,15 150,45 0,110 Z"/>
  <path class="band-bottom" d="M0,225 C110,300 240,345 320,322 C380,305 420,290 451,276 V501 H0 Z"/>
  <circle class="maker-dot" cx="138" cy="118" r="7"/>
  <text class="maker-name" x="152" y="124">Käserei Lindtal</text>
  <text class="product-word" x="225" y="228" text-anchor="middle">Polenta</text>
  <text class="variety" x="230" y="259" text-anchor="middle">TESSARA</text>
  <text class="variety" x="230" y="288" text-anchor="middle">PURA</text>
  <text class="brand-name" x="225" y="432" text-anchor="middle">Feinwahl</text>
  <text class="vegan-claim" x="225" y="473" text-anchor="middle">VEGAN</text>
</svg>

<svg class="label label--tessara-pura" viewBox="0 0 451 501" aria-label="Etikett Polenta Tessara Pura">
  <rect class="field" width="451" height="501"/>
  <path class="band-top" d="M0,0 H451 V32 C300,15 150,45 0,110 Z"/>
  <path class="band-bottom" d="M0,225 C110,300 240,345 320,322 C380,305 420,290 451,276 V501 H0 Z"/>
  <circle class="maker-dot" cx="138" cy="118" r="7"/>
  <text class="maker-name" x="152" y="124">Käserei Lindtal</text>
  <text class="product-word" x="225" y="228" text-anchor="middle">Polenta</text>
  <text class="variety" x="230" y="259" text-anchor="middle">TESSARA</text>
  <text class="variety" x="230" y="288" text-anchor="middle">PURA</text>
  <text class="brand-name" x="225" y="432" text-anchor="middle">Feinwahl</text>
  <text class="vegan-claim" x="225" y="473" text-anchor="middle">VEGAN</text>
</svg>

<svg class="label label--corvella" viewBox="0 0 451 501" aria-label="Etikett Polenta Corvella La Scelta Dorata">
  <rect class="field" width="451" height="501"/>
  <path class="band-top" d="M0,0 H451 V32 C300,15 150,45 0,110 Z"/>
  <path class="band-bottom" d="M0,225 C110,300 240,345 320,322 C380,305 420,290 451,276 V501 H0 Z"/>
  <circle class="maker-dot" cx="138" cy="118" r="7"/>
  <text class="maker-name" x="152" y="124">Käserei Lindtal</text>
  <text class="product-word" x="225" y="228" text-anchor="middle">Polenta</text>
  <text class="variety" x="230" y="259" text-anchor="middle">CORVELLA</text>
  <text class="variety" x="230" y="288" text-anchor="middle">LA SCELTA DORATA</text>
  <text class="brand-name" x="225" y="432" text-anchor="middle">Feinwahl</text>
  <text class="vegan-claim" x="225" y="473" text-anchor="middle">VEGAN</text>
</svg>

<svg class="label label--gallo-verde" viewBox="0 0 451 501" aria-label="Etikett Polenta Tessara, Gallo Verde">
  <rect class="field" width="451" height="501"/>
  <path class="band-top" d="M0,0 H451 V32 C300,15 150,45 0,110 Z"/>
  <path class="band-bottom" d="M0,225 C110,300 240,345 320,322 C380,305 420,290 451,276 V501 H0 Z"/>
  <circle class="maker-dot" cx="138" cy="118" r="7"/>
  <text class="maker-name" x="152" y="124">Käserei Lindtal</text>
  <text class="product-word" x="225" y="228" text-anchor="middle">Polenta</text>
  <text class="variety" x="230" y="259" text-anchor="middle">TESSARA</text>
  <text class="variety" x="230" y="288" text-anchor="middle">GALLO VERDE</text>
  <text class="brand-name" x="225" y="432" text-anchor="middle">Feinwahl</text>
  <text class="vegan-claim" x="225" y="473" text-anchor="middle">VEGAN</text>
</svg>

</body>
</html>
```